Brindle Structures Construction Company Seeking Modern Website

We are a small construction company wanting to create a web presence. We don't have much in the way of current content but will get photos as they come in. Attached is a picture of our business card.
The pages we would like on the menu are:
Home
Portfolio
Product Specs
Testimonials
Our Process
Contact
Some designs we like are:
http://www.tovenquarnsheds.example/
http://www.qzrsheds.example/
http://pannowsheds.example/
http://wistenhalls.example/
Not much requirements other than that so feel free to be creative!
Updates
Target Market(s)
Construction
Commercial and Residential Buildings
Industry/Entity Type
Construction Company
Number of Pages Required
5+ page
Look and feel

```html
<!DOCTYPE html>
<html lang="en">
<head>
<meta charset="utf-8">
<title>Brindle Structures</title>
<link href="https://fonts.googleapis.com/css2?family=Roboto:ital,wght@0,300;0,400;0,500;0,700;0,900;1,400;1,900&family=Lobster&display=swap" rel="stylesheet">
<style>
:root{
  --blue:#0a9bd8;
  --blue-dark:#0a6f9e;
  --ink:#1a1a1a;
  --text:#555;
  --muted:#777;
  --panel:#e6e6e6;
  --band:#ebebeb;
  --footer:#262626;
  --footer-bar:#1a1a1a;
  --white:#fff;
}
*{box-sizing:border-box;margin:0;padding:0}
html,body{width:1200px;height:2184px;overflow:hidden}
body{position:relative;background:var(--white);font-family:'Roboto',sans-serif;color:var(--text)}
.abs{position:absolute}

.site-header{left:0;top:0;width:1200px;height:150px;background:linear-gradient(#fff,#f1f1f1)}
.brand{left:73px;top:40px;display:flex;align-items:center;gap:14px}
.brand-mark{width:44px;height:44px;background:var(--blue);border-radius:50%}
.brand-name{font-size:48px;font-weight:900;color:var(--blue);letter-spacing:-1px}
.call{left:662px;top:70px;display:flex;align-items:center;gap:12px}
.call-label{font-size:15px;color:var(--ink);font-weight:500}
.call-number{font-size:32px;color:var(--blue);line-height:1}
.header-divider{left:954px;top:68px;width:1px;height:52px;background:#ccc}
.social{left:968px;top:92px;display:flex;gap:6px}
.social span{width:34px;height:34px;border:2px solid #999;border-radius:50%}

.main-nav{left:0;top:150px;width:1200px;height:44px;background:#0a0a0a;border-bottom:4px solid var(--blue);display:flex;padding-left:73px}
.main-nav a{color:#fff;text-decoration:none;font-size:16px;font-weight:500;padding:0 27px;line-height:40px;height:40px}
.main-nav a.active{background:var(--blue);padding:0 18px;margin-right:10px}

.hero{left:0;top:194px;width:1200px;height:527px;background:linear-gradient(180deg,#2f6fb8 0%,#7aa9d6 35%,#cdbfa6 60%,#5d7a3a 100%)}
.hero-title{left:80px;top:285px;font-family:'Lobster',cursive;font-size:46px;line-height:56px;color:var(--blue)}
.slide-arrow{top:414px;width:18px;height:114px;background:#888;display:flex;align-items:center;justify-content:center}
.slide-arrow.next{background:var(--blue)}
.dots{left:547px;top:680px;display:flex;gap:6px}
.dots span{width:18px;height:18px;border-radius:50%;background:#fff;border:2px solid #999}
.dots span.on{border-color:var(--blue);background:var(--blue);box-shadow:inset 0 0 0 3px #fff}
.stripe-band{left:0;top:721px;width:1200px;height:148px;background:#eeeeee}
.hero-caption{left:73px;top:689px;width:1053px;height:151px;background:#fff;box-shadow:0 2px 6px rgba(0,0,0,.15);padding:26px 24px;text-align:center;font-size:20px;line-height:28px;color:#444;font-weight:300}

.card-head{top:895px;width:514px;height:66px;background:var(--blue);display:flex;align-items:center;justify-content:center;gap:16px;color:#fff;font-size:32px;font-weight:900;font-style:italic}
.card-body{top:961px;width:494px;height:491px;background:var(--panel)}
.card-photo{top:983px;width:456px;height:257px;border:5px solid #fff;box-shadow:0 1px 4px rgba(0,0,0,.25)}
.card-text{top:1259px;width:456px;font-size:14px;line-height:21px;color:#555}
.btn{display:flex;align-items:center;justify-content:space-between;background:var(--blue-dark);color:#fff;font-size:18px;padding:0 12px 0 14px;transform:skewX(-12deg)}
.btn > *{transform:skewX(12deg)}
.card-btn{top:1425px;width:170px;height:47px}

.band{left:0;top:1510px;width:1200px;height:344px;background:var(--band)}
.band-title{top:1530px;font-size:30px;font-weight:900;font-style:italic;color:#111}
.band-rule{top:1579px;width:514px;height:4px;background:var(--blue-dark)}
.pager{top:1540px;display:flex;gap:10px}
.quote-mark{left:73px;top:1606px;width:48px;height:48px;background:#888;color:#fff;font-size:44px;font-weight:900;text-align:center;line-height:56px;font-family:Georgia,serif}
.quote-text{left:137px;top:1618px;width:450px;font-size:14px;line-height:21px;font-style:italic;color:#666}
.avatar{left:133px;top:1734px;width:52px;height:52px;border-radius:50%;background:linear-gradient(#9cc3de,#6b8fa8);border:3px solid #fff;box-shadow:0 0 0 2px var(--blue)}
.author{left:196px;top:1740px;font-size:14px;color:#222}
.author small{display:block;font-size:12px;color:#777}
.news-date{left:613px;top:1616px;font-size:12px;color:#888}
.news-head{left:613px;top:1637px;font-size:17px;color:var(--blue-dark)}
.news-text{left:613px;top:1666px;width:513px;font-size:14px;line-height:21.5px;color:#555}
.news-btn{left:616px;top:1790px;width:136px;height:36px;font-size:14px}

.footer{left:0;top:1854px;width:1200px;height:294px;background:var(--footer)}
.foot-col{top:1888px;width:240px}
.foot-col h3{font-size:18px;font-weight:500;color:#fff;padding-bottom:12px;border-bottom:1px solid #444;margin-bottom:14px}
.foot-col ul{list-style:none}
.foot-col li{font-size:14px;color:#bbb;line-height:25.5px}
.contact-item{display:flex;gap:10px;font-size:14px;color:#bbb;line-height:20px;margin-bottom:16px}
.map{width:244px;height:154px;background:linear-gradient(135deg,#eae6d9,#d8e3c9 60%,#c9d8ea)}
.keep li{display:flex;align-items:center;gap:10px;line-height:34px;margin-bottom:12px;font-size:15px;color:#ddd}
.keep li span{width:34px;height:34px;border:2px solid #ddd;border-radius:50%}
.footer-bar{left:0;top:2148px;width:1200px;height:36px;background:var(--footer-bar);font-size:13px;color:#aaa;line-height:36px;padding-left:76px}
</style>
</head>
<body>

<header class="site-header abs"></header>
<div class="brand abs"><span class="brand-mark"></span><span class="brand-name">Brindle Structures</span></div>
<div class="call abs">
  <svg width="48" height="48" viewBox="0 0 24 24" fill="none" stroke="#222" stroke-width="1.6"><path d="M6.6 3.5l3 3-2 2.5c1.4 3 3.4 5 6.4 6.4l2.5-2 3 3-2.5 2.6C11 18.6 5.4 13 3.5 6.1z"/></svg>
  <div><div class="call-label">CALL US TODAY!</div><div class="call-number">1.800.555.0142</div></div>
</div>
<div class="header-divider abs"></div>
<div class="social abs"><span></span><span></span><span></span><span></span></div>

<nav class="main-nav abs">
  <a class="active" href="#">HOME</a><a href="#">PORTFOLIO</a><a href="#">PRODUCT SPECS</a><a href="#">TESTIMONIALS</a><a href="#">OUR PROCESS</a><a href="#">CONTACT</a>
</nav>

<div class="hero abs" role="img" aria-label="Photo of a beige two-storey family house with shutters and front porch under a blue sky"></div>
<div class="hero-title abs">Building Dreams,<br>So you Can Build Memories</div>
<div class="slide-arrow abs" style="left:0"><svg width="8" height="12"><path d="M7 1L2 6l5 5" fill="#fff"/></svg></div>
<div class="slide-arrow next abs" style="left:1182px"><svg width="8" height="12"><path d="M1 1l5 5-5 5" fill="#fff"/></svg></div>
<div class="stripe-band abs"></div>
<div class="hero-caption abs">Lorem ipsum dolor sit amet, consectetur adipiscing elit, sed do eiusmod tempor incididunt ut labore et dolore magna aliqua. Ut enim ad minim veniam, quis nostrud exercitation ullamco laboris nisi ut aliquip ex ea commodo consequat. Duis aute irure dolor in reprehenderit in voluptate velit.</div>
<div class="dots abs"><span class="on"></span><span></span><span></span><span></span><span></span></div>

<div class="card-head abs" style="left:73px">
  <svg width="40" height="38" viewBox="0 0 20 19" fill="#fff"><path d="M10 1L1 9h3v9h5v-5h2v5h5V9h3z"/></svg>Residental</div>
<div class="card-body abs" style="left:83px"></div>
<div class="card-photo abs" style="left:102px;background:linear-gradient(#8fb9e0,#c7b79a 55%,#7f9a5a)" role="img" aria-label="Photo of a row of suburban family houses"></div>
<p class="card-text abs" style="left:102px">Sed ut perspiciatis unde omnis iste natus error sit voluptatem accusantium doloremque laudantium, totam rem aperiam, eaque ipsa quae ab illo inventore veritatis et quasi architecto beatae vitae dicta sunt explicabo. Nemo enim ipsam voluptatem quia voluptas sit aspernatur aut odit aut fugit, sed quia consequuntur magni dolores eos qui ratione voluptatem sequi nesciunt.</p>
<div class="btn card-btn abs" style="left:248px"><span>Learn more</span><span>&#10095;</span></div>

<div class="card-head abs" style="left:613px">
  <svg width="36" height="40" viewBox="0 0 18 20" fill="#fff"><path d="M2 1h14v19h-5v-4H7v4H2zM4 3v2h2V3zm4 0v2h2V3zm4 0v2h2V3zM4 7v2h2V7zm4 0v2h2V7zm4 0v2h2V7zM4 11v2h2v-2zm8 0v2h2v-2z"/></svg>Commercial</div>
<div class="card-body abs" style="left:623px"></div>
<div class="card-photo abs" style="left:642px;background:linear-gradient(135deg,#6fa6dd,#2f7fc8 55%,#d9dde2)" role="img" aria-label="Photo of a modern glass-fronted commercial building"></div>
<p class="card-text abs" style="left:642px">Sed ut perspiciatis unde omnis iste natus error sit voluptatem accusantium doloremque laudantium, totam rem aperiam, eaque ipsa quae ab illo inventore veritatis et quasi architecto beatae vitae dicta sunt explicabo. Nemo enim ipsam voluptatem quia voluptas sit aspernatur aut odit aut fugit, sed quia consequuntur magni dolores eos qui ratione voluptatem sequi nesciunt.</p>
<div class="btn card-btn abs" style="left:788px"><span>Learn more</span><span>&#10095;</span></div>

<section class="band abs"></section>
<h2 class="band-title abs" style="left:73px">Testimonial</h2>
<div class="pager abs" style="left:545px"><svg width="12" height="18"><path d="M10 2L3 9l7 7" stroke="#666" stroke-width="3" fill="none"/></svg><svg width="12" height="18"><path d="M2 2l7 7-7 7" stroke="var(--blue)" stroke-width="3" fill="none"/></svg></div>
<div class="band-rule abs" style="left:73px"></div>
<div class="quote-mark abs">&ldquo;</div>
<p class="quote-text abs">Sed ut perspiciatis unde omnis iste natus error sit voluptatem accusantium doloremque laudantium, totam rem aperiam, eaque ipsa quae ab illo inventore veritatis et quasi architecto beatae vitae dicta sunt explicabo. Nemo enim ipsam voluptatem quia voluptas sit aspernatur aut odit aut fugit.</p>
<div class="avatar abs" role="img" aria-label="Customer portrait"></div>
<div class="author abs">Dale Mercer<small>Happy Customer</small></div>

<h2 class="band-title abs" style="left:615px">Latest News</h2>
<div class="pager abs" style="left:1085px"><svg width="12" height="18"><path d="M10 2L3 9l7 7" stroke="#666" stroke-width="3" fill="none"/></svg><svg width="12" height="18"><path d="M2 2l7 7-7 7" stroke="var(--blue)" stroke-width="3" fill="none"/></svg></div>
<div class="band-rule abs" style="left:613px"></div>
<div class="news-date abs">10 Nov 2015</div>
<div class="news-head abs">Sed ut perspiciatis unde omnis iste natus error sit.</div>
<p class="news-text abs">Voluptatem accusantium doloremque laudantium, totam rem aperiam, eaque ipsa quae ab illo inventore veritatis et quasi architecto beatae vitae dicta sunt explicabo. totam rem aperiam, eaque ipsa quae ab illo inventore veritatis et quasi architecto beatae vitae dicta sunt explicabo. totam rem aperiam, eaque ipsa quae.</p>
<div class="btn news-btn abs"><span>Learn more</span><span>&#10095;</span></div>

<footer class="footer abs"></footer>
<div class="foot-col abs" style="left:73px"><h3>Quick Links</h3>
  <ul><li>Home</li><li>Portfolio</li><li>Product Specs</li><li>Testimonials</li><li>Our Process</li><li>Contact</li></ul></div>
<div class="foot-col abs" style="left:344px"><h3>Contact Address</h3>
  <div class="contact-item"><svg width="12" height="16" viewBox="0 0 12 16"><path d="M6 0a6 6 0 00-6 6c0 4 6 10 6 10s6-6 6-10a6 6 0 00-6-6zm0 8a2 2 0 110-4 2 2 0 010 4z" fill="#ddd"/></svg><span>228, Lorem Ipsum dolor sit,<br>Dosis amet sit - 85485</span></div>
  <div class="contact-item"><svg width="14" height="14" viewBox="0 0 24 24"><path d="M6.6 3.5l3 3-2 2.5c1.4 3 3.4 5 6.4 6.4l2.5-2 3 3-2.5 2.6C11 18.6 5.4 13 3.5 6.1z" fill="#ddd"/></svg><span>Call Us<br>1.800.555.0142</span></div>
  <div class="contact-item"><svg width="14" height="12" viewBox="0 0 14 10"><path d="M0 0h14v10H0zM1 1l6 5 6-5" fill="#ddd" stroke="#262626"/></svg><span>Email Us<br>info@brindlestructures.example</span></div></div>
<div class="foot-col abs" style="left:613px"><h3>Location Map</h3>
  <div class="map" role="img" aria-label="Street map showing the company location"></div></div>
<div class="foot-col abs" style="left:884px"><h3>Keep In Touch</h3>
  <ul class="keep"><li><span></span>Friendbook</li><li><span></span>Chirper</li><li><span></span>Circles +</li><li><span></span>Linkfolio</li></ul></div>
<div class="footer-bar abs">Copyright © 2015 Brindle Structures. | Terms of Use &nbsp;| &nbsp;Privacy Policy &nbsp;| &nbsp;Sitemap</div>

</body>
</html>
```